www.tlorvantix.com

We are a company that is in the business of extending the life of surgical equipment by repairing or refurbishing equipment to save hospitals, surgery centers and clinics money. We call ourselves Pelbrook Medical Corporation. We are in need of a website that delivers the "feel" of what of we do everyday. A website that explains our services but at the same time has a touch that is different from the rest. Many companies repair but their websites may not "pull" customers to inquire, we need that punch. At this time we are not looking for e-commerce but would like the option of adding that in the future. We do sell new and used equipment, so we like to be able to highlight those manufacturers on our site. We would like the website to have enough layouts for pictures to describe what we repair.
Target Market(s)
Biomedical Technicians and Managers, Hospital Purchasing Departments, OR Managers, type of facilities that our customer exists in, hospitals, surgery centers, clinics, animal hospitals
Industry/Entity Type
E-Commerce
Requirements
Must have
- An easy to navigate website, modern looking.
Easy to modify with pictures and or additional web pages
The winning designer to be available for future modifications and changes
Website to be unique compared to our competition, which are numerous
Nice to have
- E-Commerce capability

```html
<!DOCTYPE html>
<html lang="en">
<head>
<meta charset="utf-8">
<title>Pelbrook Medical</title>
<link href="https://fonts.googleapis.com/css2?family=Open+Sans:wght@400;600&family=PT+Sans:wght@400;700&family=Arimo:wght@400&display=swap" rel="stylesheet">
<style>
:root{
  --bg:#f4f4f4;
  --green:#4f9a22;
  --green-light:#6cb83a;
  --green-dark:#3d7f18;
  --blue:#1e5aa8;
  --blue-dark:#134683;
  --grey-text:#8a8a8a;
  --grey-dark:#666;
  --line:#dedede;
  --nav-active:#6b6b6b;
}
*{box-sizing:border-box;margin:0;padding:0}
html,body{width:1200px;height:1117px;overflow:hidden;background:var(--bg)}
body{position:relative;font-family:"Open Sans",sans-serif;color:var(--grey-text)}
.abs{position:absolute}
.brand{left:200px;top:14px;display:flex;align-items:center;gap:8px}
.brand-dot{width:36px;height:36px;border-radius:50%;background:var(--green)}
.brand-name{font-family:"PT Sans",sans-serif;font-weight:700;font-size:30px;color:var(--blue);letter-spacing:1px;white-space:nowrap}
.account{left:754px;top:8px;display:flex;gap:14px;font-size:13px;align-items:center;white-space:nowrap}
.account a{text-decoration:none;color:#aaa}
.account .signup{color:var(--green)}
.search{left:754px;top:37px;width:208px;height:29px;background:#fff;border:1px solid #d6d6d6;font-size:10px;color:#aaa;padding:8px 7px}
.search-btn{left:967px;top:37px;width:34px;height:29px;background:var(--blue);border-radius:2px}
.rule-dot{left:200px;width:800px;border-top:1px dotted #cfcfcf}
.nav{left:200px;top:89px;width:800px;height:26px;display:flex;align-items:center;font-size:11.5px;white-space:nowrap}
.nav a{color:#888;text-decoration:none;padding:0 20px;border-left:1px solid #e2e2e2;line-height:26px;white-space:nowrap}
.nav a.active{background:var(--nav-active);color:#fff;border:none;padding:0 18px}
.nav a.active + a{border-left:none}
.slider{left:200px;top:123px;width:801px;height:311px;border:3px solid #8d8d8d;background:linear-gradient(135deg,#e9eef1,#c8d2d8 50%,#aab4ba)}
.slider-shadow{left:210px;top:434px;width:780px;height:24px;background:radial-gradient(ellipse at top,rgba(0,0,0,.18),transparent 70%)}
.arrow{width:50px;height:50px;border-radius:50%;background:#1e1e1e;top:254px}
.caption{left:586px;top:335px;width:424px;height:84px;background:linear-gradient(#6cb83a,#3f8a1a);padding:14px 10px;color:#fff}
.caption h2{font-family:"PT Sans",sans-serif;font-weight:700;font-size:25px;letter-spacing:-.5px;line-height:1;white-space:nowrap}
.caption p{font-size:8.5px;margin-top:7px;line-height:1.45;color:#e4f3d8;font-family:"Arimo",sans-serif}
.caption a{color:#fff;font-size:10px}
.welcome-wrap{left:0;top:479px;width:1200px;text-align:center}
.welcome{display:inline-block;height:48px;padding:0 2px;border-top:1px dashed #bbb;border-bottom:1px dashed #bbb;font-family:"PT Sans",sans-serif;font-weight:700;font-size:36px;line-height:46px;color:#777;letter-spacing:-1.5px;white-space:nowrap}
.welcome span{color:var(--blue)}
.intro{left:198px;top:540px;width:804px;text-align:center;font-family:"Arimo",sans-serif;font-size:9.6px;line-height:14.5px}
.btn{background:linear-gradient(#2a6fc0,var(--blue-dark));color:#fff;font-family:"PT Sans",sans-serif;font-weight:700;text-align:center;border-radius:2px;white-space:nowrap}
.btn-main{left:554px;top:595px;width:94px;height:32px;font-size:14px;line-height:32px}
.rule{left:200px;width:800px;border-top:1px solid var(--line)}
.card{top:691px;width:196px;height:159px;border:2px solid var(--green);border-top:none}
.card h3{height:35px;background:linear-gradient(var(--green-light),var(--green-dark));color:#fff;font-family:"PT Sans",sans-serif;font-weight:400;font-size:19px;text-align:center;line-height:35px;letter-spacing:-.4px;white-space:nowrap}
.card .photo{height:122px}
.card-dark{border:none}
.card-dark .photo{background:linear-gradient(#2b3139,#0d0f12);padding:20px 7px;font-family:"Arimo",sans-serif;font-size:9px;line-height:13.6px;color:#c9c9c9;height:124px}
.card-dark .btn{display:inline-block;font-size:10px;padding:5px 7px;margin-top:16px}
.partners{left:200px;top:896px;width:800px;height:56px;display:flex;justify-content:space-between;align-items:center;font-family:"PT Sans",sans-serif;font-weight:700;font-size:17px;color:#222;white-space:nowrap}
.partners .p-blue{color:var(--blue)}
.partners .p-navy{color:#2b3f80}
.foot-brand{left:0;top:1000px;width:1200px;display:flex;justify-content:center;align-items:center;gap:8px}
.foot-brand .brand-dot{background:#888}
.foot-brand .brand-name{color:#777}
.foot-links{left:0;top:1067px;width:1200px;text-align:center;font-size:10px;color:#666;white-space:nowrap}
.foot-links span{margin:0 5px;color:#888}
.copy{left:0;top:1092px;width:1200px;text-align:center;font-size:9px;color:#999;white-space:nowrap}
.copy span{margin:0 4px}
.chat{left:0;top:172px;width:36px;height:109px;background:linear-gradient(90deg,#5aab2c,#3f8c1a);border:1px solid #3a7c16;border-left:none;border-radius:0 3px 3px 0}
.chat span{position:absolute;left:7px;top:78px;transform:rotate(-90deg);transform-origin:left top;color:#fff;font-size:14px;white-space:nowrap}
.social{left:1161px;top:172px;width:39px;height:123px;background:#fff;border:1px solid #ddd;border-right:none;padding:7px 0 0 8px}
.social i{display:block;width:23px;height:23px;margin-bottom:6px}
</style>
</head>
<body>
<div class="abs brand"><div class="brand-dot"></div><div class="brand-name">PELBROOK</div></div>

<div class="abs account">
  <a href="#">Cart</a><a href="#">Login</a><a href="#" class="signup">Sign Up</a>
</div>
<div class="abs search">Search...</div>
<div class="abs search-btn">
  <svg width="34" height="29" viewBox="0 0 34 29"><circle cx="15" cy="13" r="6" fill="none" stroke="#fff" stroke-width="2"/><line x1="19.5" y1="17.5" x2="25" y2="23" stroke="#fff" stroke-width="3"/></svg>
</div>

<div class="abs rule-dot" style="top:82px"></div>
<nav class="abs nav">
  <a href="#" class="active">HOME</a><a href="#">ABOUT US</a><a href="#">SERVICES</a><a href="#">REPAIR</a><a href="#">WHY CHOOSE MED</a><a href="#">VIEW FACILITY</a><a href="#">BLOG</a><a href="#">CONTACT US</a>
</nav>

<div class="abs slider-shadow"></div>
<div class="abs slider" role="img" aria-label="Operating room with surgical equipment, monitors and lights"></div>
<div class="abs arrow" style="left:216px"><svg width="50" height="50"><polyline points="29,14 19,25 29,36" fill="none" stroke="#fff" stroke-width="2"/></svg></div>
<div class="abs arrow" style="left:933px"><svg width="50" height="50"><polyline points="21,14 31,25 21,36" fill="none" stroke="#fff" stroke-width="2"/></svg></div>
<div class="abs caption">
  <h2>SURGICAL EQUIPMENT MANAGEMENT</h2>
  <p>In suscipit eleifend est nec aliquam. Suspense urna ante, faucibus vel dictum, sagitis id lorem.<br>Aenean elementum, lectus dapibus iaculis sagittis, ligula nibh sagittis torto. &nbsp;<a href="#">Learn More</a></p>
</div>

<div class="abs welcome-wrap"><h1 class="welcome">WELCOME TO <span>PELBROOK</span></h1></div>
<p class="abs intro">Lorem ipsum dolor sit amet, consectetur adipiscing elit. In suscipit eleifend est nec aliquam. Suspendisse urna ante, faucibus vel dictum in, sagittis id lorem. Aenean elementum, lectus<br>dapibus iaculis sagittis, ligula nibh sagittis tortor, vitae luctus erat lacus id ligula. Mauris malesuada laoreet mi a semper. Nullam eget justo pulvinar erat ullamcorper consequat.<br>Curabitur cursus imperdiet elit, in dictum nunc molestie ut. Praesent at iaculis magna, vel imperdiet tortor.</p>
<div class="abs btn btn-main">Learn More</div>

<div class="abs rule" style="top:658px"></div>

<div class="abs card card-dark" style="left:200px">
  <h3>Repair Services</h3>
  <div class="photo">Lorem ipsum dolor sit amet, consectetur adipiscing elit. In suscipit eleifend est nec aliquam. Suspenisse urna ante, faucibus vel dictum in, sagittis id lorem.<br><span class="btn">Learn More</span></div>
</div>
<div class="abs card" style="left:402px">
  <h3>Surgical Products</h3>
  <div class="photo" role="img" aria-label="Surgical imaging units" style="background:linear-gradient(120deg,#f2f4f6,#c9d0d6 60%,#4c6a8c)"></div>
</div>
<div class="abs card" style="left:603px">
  <h3>Pre - owned Equipment</h3>
  <div class="photo" role="img" aria-label="Warehouse of refurbished equipment" style="background:linear-gradient(160deg,#9aa7a0,#5e7566 50%,#c6c9c4)"></div>
</div>
<div class="abs card" style="left:805px">
  <h3>Repair Center</h3>
  <div class="photo" role="img" aria-label="Repair workshop interior" style="background:linear-gradient(170deg,#c9cdd1,#8f959b 55%,#3a3c3f)"></div>
</div>

<div class="abs rule" style="top:880px"></div>
<div class="abs partners">
  <span class="p-blue">Corvane Health</span>
  <span class="p-navy">Talmer</span>
  <span>Veridane</span>
  <span>Orbiscan</span>
  <span>Fennick</span>
  <span>Ostrel Vanda</span>
  <span>Halvex</span>
</div>
<div class="abs rule" style="top:964px"></div>

<div class="abs foot-brand"><div class="brand-dot"></div><div class="brand-name">PELBROOK</div></div>
<div class="abs foot-links">HOME<span>|</span>ABOUT US<span>|</span>SERVICES<span>|</span>REPAIR<span>|</span>WHY CHOSSE MED<span>|</span>VIEW FACILITY<span>|</span>BLOG<span>|</span>CONTACT US</div>
<div class="abs copy">© 2013 PELBROOK<span>|</span>Map<span>|</span>Privacy Policy<span>|</span>Term &amp; Conditions</div>

<div class="abs chat"><span>Live Chat</span></div>
<div class="abs social">
  <i style="background:#1b9bd8"></i><i style="background:#2f5a9c"></i><i style="background:#1a78b4"></i><i style="background:#d9a032"></i>
</div>
</body>
</html>
```